Rumble Deep 909s (Beat Making Expansion Pack)

Hello Designers! I'm an audio engineer and beat maker who is about to start selling sound packs on my website www.quillsofbrightmoor.com. I'm looking to have some art created for my new Sub 808 pack called "Rumble Deep 909s". I've attached some examples of another producers sound pack graphics and boxes, so you have an idea of what I'm looking for. I also have attached two pictures of cartoon booty girls to inspire the graphics I'm hoping for on my new product. I would like my product to say "www.QuillsOfBrightmoor.com Presents" at the top. At the bottom I would like my logo to go on the bottom left. Please also add the Kelo and ZX logo on the bottom right. If you have any questions please let me know.

Target Market(s)

97% of my customers are upcoming producers, 18 to 45 years old, and are guys.

Industry/Entity Type

Audio

Requirements
Must have
• Good Typography for the tittle "Rumble Deep 909s" and a picture of a fat cartoon booty.

```html
<!DOCTYPE html>
<html lang="en">
<head>
<meta charset="utf-8">
<title>Rumble Deep 909s — Pack Cover</title>
<link rel="stylesheet" href="https://fonts.googleapis.com/css2?family=Advent+Pro:wght@500;600&family=Roboto:wght@700;900&display=swap">
<style>
  :root {
    --page-bg: #a9abae;
    --band-bg: #f3f1f4;
    --ink-dark: #2a1c2a;
    --ink-purple: #6b2a72;
    --title-fill: #ffffff;
    --title-stroke: #5a1a5e;
    --art-lavender: #b9aec4;
    --art-grey: #d9d6db;
    --art-berry: #8e1f5a;
    --art-orange: #e7874a;
    --art-violet: #5a3c8e;
  }
  * { margin: 0; padding: 0; box-sizing: border-box; }
  html, body {
    width: 1200px;
    height: 900px;
    overflow: hidden;
    background: var(--page-bg);
  }
  .cover {
    position: absolute;
    left: 345px;
    top: 40px;
    width: 510px;
    height: 820px;
    background: var(--band-bg);
    overflow: hidden;
    box-shadow: 0 10px 30px rgba(0,0,0,0.25);
  }
  .cover__header {
    position: absolute;
    left: 0; top: 0;
    width: 100%;
    height: 70px;
    text-align: center;
    padding-top: 18px;
    font-family: "Roboto", Arial, sans-serif;
  }
  .cover__url {
    color: var(--ink-dark);
    font-weight: 900;
    font-size: 17px;
    letter-spacing: 0.04em;
  }
  .cover__presents {
    margin-top: 4px;
    color: var(--ink-purple);
    font-weight: 700;
    font-size: 12px;
    letter-spacing: 0.55em;
  }
  .cover__art {
    position: absolute;
    left: 0; top: 70px;
    width: 100%;
    height: 750px;
    background:
      radial-gradient(ellipse 38% 22% at 62% 30%, var(--art-berry) 0%, rgba(142,31,90,0.7) 55%, transparent 100%),
      radial-gradient(ellipse 42% 26% at 40% 58%, var(--art-orange) 0%, rgba(231,135,74,0.6) 55%, transparent 100%),
      radial-gradient(ellipse 20% 30% at 45% 88%, var(--art-violet) 0%, transparent 100%),
      radial-gradient(ellipse 12% 10% at 4% 24%, #8c72c6 0%, transparent 100%),
      linear-gradient(160deg, var(--art-grey) 0%, var(--art-lavender) 55%, #d8d3dc 100%);
  }
  .cover__title {
    position: absolute;
    right: 18px;
    top: 255px;
    text-align: left;
    font-family: "Advent Pro", "Arial Narrow", sans-serif;
    font-weight: 600;
    color: var(--title-fill);
    -webkit-text-stroke: 5px var(--title-stroke);
    paint-order: stroke fill;
    line-height: 0.9;
  }
  .cover__title-top {
    display: block;
    font-size: 84px;
    letter-spacing: -0.01em;
  }
  .cover__title-num {
    display: block;
    font-size: 196px;
    letter-spacing: -0.02em;
  }
  .cover__brand {
    position: absolute;
    left: 24px;
    bottom: 26px;
    font-family: "Roboto", Arial, sans-serif;
    font-weight: 900;
    font-size: 18px;
    color: var(--title-fill);
  }
  .cover__platforms {
    position: absolute;
    right: 22px;
    bottom: 230px;
    display: flex;
    gap: 10px;
    align-items: center;
    font-family: "Roboto", Arial, sans-serif;
    font-weight: 900;
    font-size: 14px;
    color: var(--ink-dark);
  }
  .platform {
    display: flex;
    align-items: center;
    gap: 4px;
  }
  .platform__mark {
    width: 10px;
    height: 10px;
    background: var(--art-berry);
  }
</style>
</head>
<body>
  <main class="cover">
    <header class="cover__header">
      <p class="cover__url">www.QuillsOfBrightmoor.com</p>
      <p class="cover__presents">PRESENTS</p>
    </header>

    <div class="cover__art" role="img" aria-label="Cartoon illustration of a curvy figure in berry shorts on a lavender backdrop"></div>

    <h1 class="cover__title">
      <span class="cover__title-top">Rumble Deep</span>
      <span class="cover__title-num">909s</span>
    </h1>

    <div class="cover__platforms">
      <span class="platform"><span class="platform__mark"></span>ZX</span>
      <span class="platform">Kelo</span>
    </div>

    <p class="cover__brand">Quills Of Brightmoor</p>
  </main>
</body>
</html>
```